Safety training business card design

We need a buisness card design and logo for a small buisness that provides safety training through out the mining and civil construction industries. We provide first aid , confined space working at heights , machinery tickets, chainsaw, four wheel drive and four wheel motorbike training. We would like to use the design colors of navy blue, Fluro or lime green and white .

Industry/Entity Type

Construction

Contact Information for Business Card

Kelbrook Earthmoving & Training , Dennis Holloway, kelbrook.training@mailbox-example.com, ph 0438615044 abn 47 816 305 971

```html
<!DOCTYPE html>
<html lang="en">
<head>
<meta charset="utf-8">
<title>Kelbrook Earthmoving &amp; Training – Business Card</title>
<link rel="stylesheet" href="https://fonts.googleapis.com/css2?family=Tinos&display=swap">
<style>
  :root {
    --lime: #76c043;
    --lime-deep: #66b035;
    --lime-faint: #e3f1d8;
    --white: #ffffff;
    --page: #eeeeea;
    --ink-light: #ffffff;
  }
  * { margin: 0; padding: 0; box-sizing: border-box; }
  html, body {
    width: 1200px; height: 1000px; overflow: hidden;
    background: var(--page);
    font-family: "Tinos", "Times New Roman", serif;
  }
  .canvas { position: relative; width: 1200px; height: 1000px; }
  .card {
    position: absolute; left: 280px; width: 640px; height: 380px;
    border-radius: 18px; overflow: hidden;
    box-shadow: 0 2px 8px rgba(0,0,0,.18);
  }
  .card-front { top: 70px; background: var(--lime); }
  .card-back { top: 540px; background: var(--white); }

  .brand-mark {
    position: absolute; left: 50%; top: 70px; transform: translateX(-50%);
    width: 130px; height: 130px; border-radius: 50%; background: var(--white);
  }
  .brand-name {
    position: absolute; left: 0; right: 0; top: 250px;
    text-align: center; color: var(--ink-light); font-size: 27px;
  }

  .back-mark {
    position: absolute; left: 215px; top: 40px; width: 300px; height: 300px;
    border-radius: 50%; background: var(--lime-faint); opacity: .7;
  }
  .back-heading {
    position: absolute; left: 0; right: 0; top: 60px; text-align: center;
    color: var(--lime); font-size: 26px; line-height: 1.12;
  }
  .contact-band {
    position: absolute; left: 0; right: 0; top: 175px; height: 145px;
    background: var(--lime); opacity: .95;
  }
  .contact {
    position: absolute; display: flex; align-items: center; gap: 10px;
    color: var(--ink-light); font-size: 23px; white-space: nowrap;
  }
  .contact svg { flex: none; }
  .contact-phone { right: 50px; top: 190px; }
  .contact-abn { left: 55px; top: 240px; }
  .contact-email { left: 55px; top: 282px; font-size: 21px; }
</style>
</head>
<body>
<main class="canvas">
  <section class="card card-front" aria-label="Business card front">
    <div class="brand-mark"></div>
    <p class="brand-name">Kelbrook Earthmoving &amp; Training</p>
  </section>

  <section class="card card-back" aria-label="Business card back">
    <div class="back-mark"></div>
    <h1 class="back-heading">Kelbrook Earthmoving &amp; Training<br>Dennis Holloway</h1>
    <div class="contact-band"></div>

    <p class="contact contact-phone">
      <svg width="18" height="24" viewBox="0 0 18 24" aria-hidden="true">
        <path d="M4 1 L8 1 L9 7 L6 9 Q7 14 11 17 L13 14 L18 16 L17 21 Q14 24 9 21 Q2 15 1 7 Q1 3 4 1 Z" fill="var(--white)"/>
      </svg>
      0438 615 044
    </p>
    <p class="contact contact-abn">
      <svg width="32" height="26" viewBox="0 0 32 26" aria-hidden="true">
        <rect x="1" y="1" width="30" height="24" rx="5" fill="none" stroke="var(--white)" stroke-width="2"/>
        <text x="16" y="17" text-anchor="middle" font-size="9" fill="var(--white)" font-family="Tinos, serif">ABN</text>
      </svg>
      47 816 305 971
    </p>
    <p class="contact contact-email">
      <svg width="28" height="20" viewBox="0 0 28 20" aria-hidden="true">
        <rect x="1" y="1" width="26" height="18" fill="none" stroke="var(--white)" stroke-width="2"/>
        <path d="M1 1 L14 11 L27 1" fill="none" stroke="var(--white)" stroke-width="2"/>
      </svg>
      kelbrook.training@mailbox-example.com
    </p>
  </section>
</main>
</body>
</html>
```